Personal development products that change your life

This is a direct selling business that sells personal development courses, but also sells the business as well if desired. This is not MLM, and there is no handling of the product required, nor hassling friends or family. We are looking for business minded people wanting to work their own hours and achieve a desirable income from this. A success image or happy image on a flyer would be great. I'd like the website address to be displayed as well thanks. www.gainpath-hub.com.au

Target Market(s)

Business-minded individuals searching for more finances. Self motivated, driven, interested in self development.

Industry/Entity Type

Business

Font styles to use
Sans Serif

Requirements
Must have
• Are you looking for
• - a franchise or business?
• - a change of career?
• - a back up income?
• Not MLM
• No product handling or shipping
• No hard sales required
• website: www.gainpath-hub.com.au
Nice to have
• A picture or background of excited person jumping in the air, or some similar.
• Worded to enrol people interested in achieving more financial headway, or flexible hours, or travel and do this business from anywhere in the world.
• Only need access to a phone, internet connection and a desire to succeed.

```html
<!DOCTYPE html>
<html lang="en">
<head>
<meta charset="utf-8">
<title>GainPath Hub – Flyer</title>
<link rel="stylesheet" href="https://fonts.googleapis.com/css2?family=Raleway:wght@300;400;800&display=swap">
<style>
  :root {
    --page-bg: #e9ecf2;
    --sky-deep: #3d7cc9;
    --sky-mid: #74a9e0;
    --sky-light: #bcd8f3;
    --sky-white: #ffffff;
    --navy: #23398a;
    --band-light: #b4d3ee;
    --band-deep: #6cb0e4;
    --periwinkle: #8ea6dc;
    --periwinkle-deep: #7d98d3;
    --periwinkle-pale: #a9c0e8;
    --white: #ffffff;
    --rule: rgba(255, 255, 255, 0.55);
  }

  html, body {
    margin: 0;
    padding: 0;
    width: 1200px;
    height: 960px;
    overflow: hidden;
    background: var(--page-bg);
    font-family: "Raleway", Arial, sans-serif;
  }

  .flyer {
    position: absolute;
    left: 282px;
    top: 30px;
    width: 636px;
    height: 900px;
    overflow: hidden;
    background: var(--periwinkle);
  }

  .hero-photo {
    position: absolute;
    left: 0;
    top: 0;
    width: 636px;
    height: 640px;
    background:
      radial-gradient(ellipse 420px 360px at 640px 330px, var(--sky-white) 0%, rgba(255,255,255,0.85) 35%, rgba(255,255,255,0) 75%),
      linear-gradient(160deg, var(--sky-deep) 0%, var(--sky-mid) 45%, var(--sky-light) 80%);
  }

  .shapes {
    position: absolute;
    left: 0;
    top: 0;
    width: 636px;
    height: 900px;
  }

  .headline {
    position: absolute;
    left: 227px;
    top: 49px;
    width: 400px;
    margin: 0;
    text-align: center;
    font-weight: 800;
    font-size: 54px;
    line-height: 54px;
    color: var(--white);
    letter-spacing: 0.5px;
  }

  .question {
    position: absolute;
    margin: 0;
    font-weight: 400;
    font-size: 24px;
    line-height: 28px;
    color: var(--navy);
    white-space: nowrap;
  }
  .question--franchise { right: 75px; top: 222px; }
  .question--career { right: 162px; top: 259px; }
  .question--income { right: 55px; top: 299px; }

  .benefit {
    position: absolute;
    margin: 0;
    font-weight: 300;
    color: var(--white);
    white-space: nowrap;
  }
  .benefit--mlm { left: 393px; top: 393px; font-size: 29px; line-height: 34px; }
  .benefit--shipping { left: 223px; top: 449px; font-size: 23px; line-height: 28px; }
  .benefit--sales { left: 324px; top: 500px; font-size: 23px; line-height: 28px; }

  .body-copy {
    position: absolute;
    left: 49px;
    top: 528px;
    width: 560px;
    font-weight: 400;
    font-size: 14.5px;
    line-height: 21px;
    color: rgba(255, 255, 255, 0.92);
  }
  .body-copy p { margin: 0 0 21px 0; }
  .body-copy .tagline { margin-top: 43px; }

  .website {
    position: absolute;
    left: 0;
    top: 832px;
    width: 636px;
    margin: 0;
    text-align: center;
    font-size: 13.5px;
    font-weight: 400;
    color: var(--navy);
    letter-spacing: 0.3px;
  }
</style>
</head>
<body>
  <main class="flyer">
    <div class="hero-photo" role="img" aria-label="Photo of a happy woman jumping in the air against a bright blue sky with white clouds"></div>

    <svg class="shapes" viewBox="0 0 568 803" preserveAspectRatio="none" aria-hidden="true">
      <defs>
        <linearGradient id="bandFill" x1="0" y1="0" x2="0" y2="1">
          <stop offset="0" stop-color="var(--band-light)"/>
          <stop offset="1" stop-color="var(--band-deep)"/>
        </linearGradient>
        <linearGradient id="baseFill" x1="0" y1="0" x2="0" y2="1">
          <stop offset="0" stop-color="var(--periwinkle)"/>
          <stop offset="0.55" stop-color="var(--periwinkle-deep)"/>
          <stop offset="1" stop-color="var(--periwinkle-pale)"/>
        </linearGradient>
      </defs>
      <path class="benefit-band" d="M0 403 L515 323 Q548 318 568 332 L568 543 Z" fill="url(#bandFill)"/>
      <path class="base-panel" d="M0 403 L568 543 L568 803 L0 803 Z" fill="url(#baseFill)"/>
      <g class="band-rules" stroke="var(--rule)" stroke-width="0.8">
        <line x1="330" y1="336" x2="568" y2="336"/>
        <line x1="150" y1="387" x2="568" y2="387"/>
        <line x1="120" y1="433" x2="568" y2="433"/>
        <line x1="260" y1="478" x2="568" y2="478"/>
      </g>
    </svg>

    <h1 class="headline">Are you<br>looking<br>for</h1>

    <p class="question question--franchise">a franchise or business?</p>
    <p class="question question--career">a change of career?</p>
    <p class="question question--income">a back up income?</p>

    <p class="benefit benefit--mlm">Not MLM</p>
    <p class="benefit benefit--shipping">No product handling or shipping</p>
    <p class="benefit benefit--sales">No hard sales required</p>

    <div class="body-copy">
      <p>We supply you<br>with the simple and complete<br>business model and all of your training and<br>support is only a phone call away.</p>
      <p>You provide the desire, motivation and willingness to learn and have a real<br>passion for wanting a huge change, personally and financially, in your life.</p>
      <p class="tagline">Start the work / life balance you've always wanted.</p>
    </div>

    <p class="website">www.gainpath-hub.com.au</p>
  </main>
</body>
</html>
```